Update Business Card Design

I'm looking to update my business cards. Attached is a photo of the current design. I like the black side so that does not have to be update. The white side needs to be updated. I want the design to be modern and minimalistic.
I am a lawyer and my firm's website is www.brennoxlegalco.com (for reference).
My firm's logo has a horizontal version (which is on the black side of the card) and a vertical version (on the white side). I would prefer to keep the vertical version on the white side and horizontal version on the black side (the logo files are attached).

I am open to redesigning the black side also. I would like one side to have the horizontal logo and the other to have the vertical logo.

```html
<!DOCTYPE html>
<html lang="en">
<head>
<meta charset="utf-8">
<title>Brennox Legal Co — Business Card</title>
<link rel="stylesheet" href="https://fonts.googleapis.com/css2?family=Arimo:wght@400;700&family=Crimson+Text:wght@400;600&family=Cinzel:wght@400&display=swap">
<style>
  :root {
    --backdrop: #3e3e3e;
    --card-white: #ffffff;
    --card-black: #1d1d1d;
    --brand-cyan: #00b4e0;
    --band-cyan: #00a9d2;
    --ink-grey: #5a5a5a;
    --ink-dark: #111111;
    --rule-grey: #555555;
    --paper-white: #ececec;
  }
  * { margin: 0; padding: 0; box-sizing: border-box; }
  html, body { width: 1200px; height: 1059px; overflow: hidden; }
  body { background: var(--backdrop); position: relative; font-family: "Arimo", Arial, sans-serif; }

  .card { position: absolute; left: 232px; width: 737px; height: 421px; overflow: hidden; }
  .card--front { top: 91px; background: var(--card-white); }
  .card--back { top: 563px; background: var(--card-black); }

  /* Front: vertical brand lockup */
  .brand-vertical { position: absolute; left: 76px; top: 52px; width: 200px; text-align: center; }
  .brand-vertical__dot { width: 120px; height: 120px; border-radius: 50%; background: var(--brand-cyan); margin: 0 auto; }
  .brand-vertical__rule { width: 192px; height: 3px; background: var(--rule-grey); border-radius: 50%; margin: 55px auto 0; }
  .brand-vertical__name {
    font-family: "Arimo", Arial, sans-serif; font-weight: 400; color: var(--brand-cyan);
    font-size: 32px; line-height: 44px; margin-top: 12px;
  }

  .divider { position: absolute; left: 311px; top: 91px; width: 2px; height: 197px; background: var(--brand-cyan); }

  .contact { position: absolute; left: 343px; top: 86px; }
  .contact__name { font-family: "Crimson Text", Georgia, serif; font-weight: 600; font-size: 38px; line-height: 44px; color: var(--brand-cyan); }
  .contact__title { font-size: 19px; color: var(--ink-grey); }
  .contact__line { display: flex; align-items: center; gap: 9px; font-size: 19px; color: var(--ink-dark); height: 29px; }
  .contact__line--first { margin-top: 30px; }
  .contact__phone { font-weight: 700; }
  .contact__line svg { width: 18px; height: 18px; flex: none; }
  .contact__address { font-size: 19px; line-height: 27px; color: var(--ink-grey); margin-top: 12px; }

  .footer-band { position: absolute; left: 0; bottom: 0; width: 737px; height: 15px; background: var(--band-cyan); }
  .footer-tab { position: absolute; left: 0; top: 382px; width: 737px; height: 39px; }
  .footer-text {
    position: absolute; left: 0; width: 737px; top: 387px; text-align: center;
    font-weight: 700; font-size: 20px; color: var(--card-white);
  }
  .footer-text .sep { margin: 0 10px; }

  /* Back: horizontal brand lockup */
  .brand-horizontal { position: absolute; left: 200px; top: 133px; display: flex; align-items: center; }
  .brand-horizontal__dot { width: 104px; height: 104px; border-radius: 50%; background: var(--brand-cyan); }
  .brand-horizontal__rule { width: 2px; height: 100px; background: var(--paper-white); margin: 0 20px 0 24px; opacity: 0.85; }
  .brand-horizontal__name {
    font-family: "Arimo", Arial, sans-serif; font-weight: 400; color: var(--brand-cyan);
    font-size: 38px; line-height: 48px;
  }
  .web-address {
    position: absolute; left: 0; width: 737px; top: 256px; text-align: center;
    font-family: "Cinzel", "Times New Roman", serif; font-size: 21px; color: var(--paper-white); letter-spacing: 0.3px;
  }
</style>
</head>
<body>
  <section class="card card--front">
    <div class="brand-vertical">
      <div class="brand-vertical__dot"></div>
      <div class="brand-vertical__rule"></div>
      <div class="brand-vertical__name">BRENNOX<br>LEGAL CO</div>
    </div>

    <div class="divider"></div>

    <div class="contact">
      <div class="contact__name">Darian Holloway</div>
      <div class="contact__title">Attorney at Law</div>
      <div class="contact__line contact__line--first contact__phone">
        <svg viewBox="0 0 24 24" aria-hidden="true"><path fill="#00b4e0" d="M6.6 10.8a15.1 15.1 0 0 0 6.6 6.6l2.2-2.2a1 1 0 0 1 1-.25 11.4 11.4 0 0 0 3.6.57 1 1 0 0 1 1 1V20a1 1 0 0 1-1 1A17 17 0 0 1 3 4a1 1 0 0 1 1-1h3.5a1 1 0 0 1 1 1c0 1.25.2 2.450.57 3.57a1 1 0 0 1-.25 1z"/><path fill="none" stroke="#00b4e0" stroke-width="2" d="M14 3a7 7 0 0 1 7 7M14 7a3 3 0 0 1 3 3"/></svg>
        <span>310.555.0148</span>
      </div>
      <div class="contact__line">
        <svg viewBox="0 0 24 24" aria-hidden="true"><path fill="#00b4e0" d="M22 2 2 10l7 3 10-8-8 9v7l4-5 4 3z"/></svg>
        <span>darian@brennoxlegalco.com</span>
      </div>
      <div class="contact__address">1180 Marlow Avenue, Suite 310<br>Westbrook, CA 90418</div>
    </div>

    <div class="footer-band"></div>
    <svg class="footer-tab" viewBox="0 0 737 39" aria-hidden="true">
      <defs>
        <linearGradient id="tabFill" x1="0" x2="1" y1="0" y2="0">
          <stop offset="0" stop-color="#00b0dc"/>
          <stop offset="0.5" stop-color="#14d0fb"/>
          <stop offset="1" stop-color="#00b0dc"/>
        </linearGradient>
      </defs>
      <polygon points="155,0 582,0 614,39 120,39" fill="url(#tabFill)"/>
    </svg>
    <div class="footer-text">T. 310.555.0172<span class="sep">|</span>F. 310.555.0186</div>
  </section>

  <section class="card card--back">
    <div class="brand-horizontal">
      <div class="brand-horizontal__dot"></div>
      <div class="brand-horizontal__rule"></div>
      <div class="brand-horizontal__name">BRENNOX<br>LEGAL CO</div>
    </div>
    <div class="web-address">www.brennoxlegalco.com</div>
  </section>
</body>
</html>
```